WEBSITE DESIGN - www.brondellix.com

We need a professional and modern looking website for our business. The current website was only made tentatively and can be viewed (we expect a website MUCH better than this). It needs to be simple and non-cluttered yet look modern and sophisticated. It needs to be very easy to navigate as our tarket market is people over the age of 45. Our logo is attached below and this should be incorporated plus the colours/theme should match this. We don't mind purchasing images online if your design includes these and we like it.

Any other specific questions please enquire as we want to hear them.

Target Market(s)

over 45 age english speaking westerners

Industry/Entity Type

Business

Number of Pages Required

1 page

Requirements
Must have
• -our logo (attached).
• -page tabs as those described (tabs.. but not necessarily each of these pages completed as well although this would be nice).
• -social media logos
• Pages should include: homepage, services, pricing, about us, contact us. There should also be a payments page designed which would link with the other pages but there would be no tab for this.

```html
<!DOCTYPE html>
<html lang="en">
<head>
<meta charset="utf-8">
<title>Brondellix – Instant Tech Support</title>
<link rel="stylesheet" href="https://fonts.googleapis.com/css2?family=Roboto:wght@400;500;700&family=Roboto+Condensed:wght@400;700&family=Bitter:wght@700&display=swap">
<style>
:root{
  --brown:#9a5a0d;
  --brown-dark:#7e4707;
  --gold:#d79a14;
  --sun:#f5c95c;
  --ink:#111;
  --text:#333;
  --muted:#666;
  --white:#fff;
  --light:#ececec;
  --black:#050505;
}
*{box-sizing:border-box;margin:0;padding:0}
html,body{width:1200px;height:3203px;overflow:hidden}
body{font-family:"Roboto",sans-serif;color:var(--text);background:var(--white);position:relative}
section,header,footer{position:absolute;left:0;width:1200px}
h2.section-title{font-family:"Roboto Condensed",sans-serif;font-weight:700;font-size:34px;color:var(--ink);text-align:center;letter-spacing:.3px}
h2.section-title small{font-family:"Roboto",sans-serif;font-weight:400;font-size:13px;margin-left:6px;letter-spacing:0}

/* header */
.site-header{top:0;height:77px;background:var(--white);border-bottom:1px solid #ddd}
.brand{position:absolute;left:210px;top:18px;display:flex;align-items:center;gap:10px}
.brand-mark{width:26px;height:26px;background:var(--brown)}
.brand-name{font-family:"Roboto",sans-serif;font-weight:500;font-size:26px;color:var(--brown)}
.top-contact{position:absolute;right:90px;top:10px;font-size:10px;color:var(--muted);display:flex;gap:22px}
.main-nav{position:absolute;right:90px;top:40px;display:flex;gap:38px;font-family:"Roboto Condensed",sans-serif;font-size:17px;color:var(--ink)}
.main-nav .active{color:var(--brown)}

/* hero */
.hero{top:77px;height:397px;background:linear-gradient(100deg,#3a2a1f 0%,#7a5d48 35%,#5a4537 60%,#2c221c 100%)}
.hero-title{position:absolute;top:135px;width:100%;text-align:center;font-family:"Roboto Condensed",sans-serif;font-weight:700;font-size:60px;color:var(--white)}
.hero-sub{position:absolute;top:208px;width:100%;text-align:center;font-size:21px;color:var(--sun)}
.hero-arrow{position:absolute;top:170px;width:38px;height:38px}
.hero-arrow.prev{left:70px}.hero-arrow.next{right:52px}
.call-bar{top:474px;height:77px;background:var(--black)}
.call-text{position:absolute;left:193px;top:23px;font-size:25px;color:var(--white)}
.call-text em{font-style:normal;color:var(--sun)}
.call-button{position:absolute;left:728px;top:8px;width:275px;height:62px;background:var(--brown);transform:skewX(-14deg);border:2px solid var(--sun)}
.call-button span{display:block;transform:skewX(14deg);font-family:"Roboto Condensed",sans-serif;font-weight:700;font-size:28px;color:var(--white);text-align:center;line-height:58px}

/* intro */
.intro{top:551px;height:192px}
.intro h2{margin-top:38px}
.intro p{width:860px;margin:10px auto 0;text-align:center;font-size:13px;line-height:20px}

/* stats */
.stats{top:743px;height:218px;background:var(--brown);display:flex;justify-content:center;gap:0}
.stat{width:176px;text-align:center;color:var(--white);padding-top:40px}
.stat-icon{width:64px;height:64px;border-radius:50%;background:var(--white);margin:0 auto;display:flex;align-items:center;justify-content:center}
.stat-num{font-size:32px;margin-top:12px}
.stat-label{font-size:12px;margin-top:2px}

/* why */
.why{top:961px;height:380px}
.why h2{margin-top:27px}
.why p{text-align:center;font-size:13px;line-height:19px;margin-top:12px}
.why-cards{position:absolute;top:139px;left:194px;display:flex;gap:23px}
.why-card{width:185px;height:201px;position:relative;color:var(--white)}
.why-card .card-label{position:absolute;left:0;right:0;bottom:0;height:44px;background:rgba(0,0,0,.75);font-family:"Roboto Condensed",sans-serif;font-weight:700;font-size:16px;text-align:center;line-height:44px}
.why-card.top-label .card-label{top:0;bottom:auto;background:rgba(0,0,0,.55)}
.card-photo{position:absolute;inset:0}
.why-card.text-card{background:var(--brown);padding:26px 18px;text-align:center}
.text-card h3{font-family:"Roboto Condensed",sans-serif;font-size:16px;border-bottom:1px solid rgba(255,255,255,.6);padding-bottom:8px}
.text-card p{font-size:12px;line-height:17px;margin-top:12px;color:var(--white)}

/* services */
.services{top:1341px;height:314px;background:var(--sun)}
.services h2{margin-top:32px}
.service-list{position:absolute;top:93px;left:195px;display:flex;gap:0}
.service{width:204px;text-align:center}
.service-icon{width:92px;height:92px;border-radius:50%;background:var(--brown);margin:0 auto;display:flex;align-items:center;justify-content:center}
.service h3{font-family:"Roboto Condensed",sans-serif;font-size:16px;color:var(--ink);margin-top:14px}
.service p{font-size:11px;line-height:16px;color:#3a2a10;margin:4px 14px 0}

/* testimonials */
.testimonials{top:1655px;height:324px;background:var(--black);color:var(--white)}
.testimonials h2{color:var(--white);margin-top:30px}
.client-photo{position:absolute;top:96px;left:557px;width:86px;height:86px;border-radius:50%;background:radial-gradient(circle at 50% 40%,#e3c9a8,#b58e69);border:3px solid #fff}
.client-name{position:absolute;top:183px;width:100%;text-align:center;font-size:10px}
.quote{position:absolute;top:222px;left:330px;width:540px;text-align:center;font-size:11px;line-height:17px}
.quote-mark{position:absolute;top:206px;font-family:"Bitter",serif;font-size:40px;color:#999}
.dots{position:absolute;top:283px;width:100%;display:flex;justify-content:center;gap:5px}
.dots i{width:8px;height:8px;border-radius:50%;border:1px solid #fff;display:block}
.dots i.on{background:#fff}

/* pricing */
.pricing{top:1979px;height:466px}
.pricing h2{margin-top:26px}
.plans{position:absolute;top:88px;left:280px;display:flex}
.plan{width:218px;padding:0 16px 0 16px}
.plan-head{margin:0 -16px;height:44px;display:flex;justify-content:space-between;align-items:center;padding:0 16px;color:var(--white);font-size:14px}
.plan-head small{font-size:9px}
.plan.quick .plan-head{background:var(--black)}
.plan.starter .plan-head{background:var(--gold)}
.plan.yearly .plan-head{background:var(--brown)}
.plan-price{font-family:"Bitter",serif;font-size:24px;line-height:28px;margin-top:14px;color:var(--ink)}
.plan.starter .plan-price{color:var(--gold)}
.plan.yearly .plan-price{color:var(--brown)}
.plan-note{font-size:8.5px;line-height:12px;color:var(--muted);margin-top:8px}
.plan-features{font-size:8.5px;line-height:12px;color:var(--muted);margin-top:10px;list-style:none}
.plan-terms{font-size:8.5px;color:var(--brown);margin-top:8px;display:flex;align-items:center;gap:4px}
.plan-terms i{width:8px;height:8px;border:1px solid var(--muted);display:block}
.plan-order{margin-top:14px;width:88px;height:22px;border:2px solid var(--ink);font-size:9px;text-align:center;line-height:18px;color:var(--ink)}
.plan.starter .plan-order{border-color:var(--gold);color:var(--gold)}
.plan.yearly .plan-order{border-color:var(--brown);color:var(--brown)}

/* contact */
.contact{top:2445px;height:352px;background:var(--light)}
.map{position:absolute;left:0;top:0;width:583px;height:352px;background:linear-gradient(135deg,#e6e2d8,#d5dbe3 55%,#c9d6e6)}
.contact h2{position:absolute;left:583px;width:617px;top:30px;margin:0}
.contact-cards{position:absolute;left:620px;top:104px;display:flex}
.contact-card{width:188px;text-align:center;font-size:8.5px;line-height:13px;color:var(--text)}
.contact-icon{width:55px;height:55px;margin:0 auto 10px;display:flex;align-items:center;justify-content:center}
.contact-card.addr .contact-icon{background:var(--black)}
.contact-card.phone .contact-icon{background:var(--gold)}
.contact-card.mail .contact-icon{background:var(--brown)}
.contact-card b{display:block;font-weight:500;margin-bottom:6px;font-size:8px}
.socials{position:absolute;left:800px;top:283px;display:flex;gap:15px}
.socials span{width:32px;height:32px;background:#a58c66;display:block}

/* register */
.register{top:2797px;height:337px;background:var(--brown)}
.register h2{color:var(--white);margin-top:30px;font-size:30px}
.form{position:absolute;top:105px;left:318px;display:grid;grid-template-columns:273px 269px;column-gap:20px;row-gap:11px}
.field{height:32px;background:var(--white);font-size:11px;color:#888;padding:0 10px;line-height:32px;position:relative}
.field.select::after{content:"";position:absolute;right:10px;top:13px;border:6px solid transparent;border-top-color:#333}
.submit{position:absolute;top:282px;left:555px;width:90px;height:30px;background:var(--black);color:var(--white);font-size:11px;text-align:center;line-height:30px}

/* footer */
.site-footer{top:3134px;height:69px;background:var(--white)}
.footer-brand{position:absolute;left:195px;top:22px;display:flex;align-items:center;gap:7px}
.footer-brand .brand-mark{width:16px;height:16px}
.footer-brand .brand-name{font-size:17px}
.copyright{position:absolute;left:315px;top:28px;font-size:10px;color:#888}
.footer-nav{position:absolute;right:190px;top:27px;display:flex;gap:38px;font-size:11px;color:var(--ink)}
.footer-nav .active{color:var(--brown)}
</style>
</head>
<body>

<header class="site-header">
  <div class="brand"><span class="brand-mark"></span><span class="brand-name">Brondellix</span></div>
  <div class="top-contact"><span>CALL US | +1 555 010 4821</span><span>EMAIL | info@brondellix.com</span></div>
  <nav class="main-nav"><span class="active">HOME</span><span>SERVICES</span><span>PRICING</span><span>ABOUT US</span><span>CONTACT</span></nav>
</header>

<section class="hero" role="img" aria-label="Support agents wearing headsets answering customer calls">
  <svg class="hero-arrow prev" viewBox="0 0 38 38"><rect width="38" height="38" fill="rgba(0,0,0,.4)"/><path d="M23 11 15 19l8 8" stroke="#d79a14" stroke-width="4" fill="none"/></svg>
  <div class="hero-title">INSTANT SUPPORT</div>
  <div class="hero-sub">Instant Technical Help For Your Devices.</div>
  <svg class="hero-arrow next" viewBox="0 0 38 38"><rect width="38" height="38" fill="rgba(0,0,0,.4)"/><path d="M15 11l8 8-8 8" stroke="#d79a14" stroke-width="4" fill="none"/></svg>
</section>

<section class="call-bar">
  <div class="call-text"><em>Call us</em> Today for Instant Tech Support <em>NOW!</em></div>
  <div class="call-button"><span>CONTACT NOW &#9656;</span></div>
</section>

<section class="intro">
  <h2 class="section-title">OUR CUSTOMER OUR PRIORITY</h2>
  <p>Lets Say Hi..<br>Brondellix was established to provide consumers with access to the sophisticated, enterprise-level IT services, support and the benefits and cost savings available to larger organisations. We provide proactive monitoring and management of customers entire IT needs. Brondellix is a growing organisation dedicated to making your PC tech support easy and accessible.</p>
</section>

<section class="stats">
  <div class="stat"><div class="stat-icon"><svg width="34" height="34" viewBox="0 0 34 34"><rect x="6" y="8" width="22" height="15" fill="none" stroke="#9a5a0d" stroke-width="2.5"/><rect x="3" y="24" width="28" height="3" fill="#9a5a0d"/></svg></div><div class="stat-num">986</div><div class="stat-label">Laptops</div></div>
  <div class="stat"><div class="stat-icon"><svg width="34" height="34" viewBox="0 0 34 34"><rect x="5" y="17" width="24" height="9" fill="#9a5a0d"/><path d="M10 16V8M24 16V8" stroke="#9a5a0d" stroke-width="2"/></svg></div><div class="stat-num">256</div><div class="stat-label">Routers</div></div>
  <div class="stat"><div class="stat-icon"><svg width="34" height="34" viewBox="0 0 34 34"><rect x="11" y="5" width="12" height="24" rx="2" fill="none" stroke="#9a5a0d" stroke-width="2.5"/><circle cx="17" cy="25" r="1.3" fill="#9a5a0d"/></svg></div><div class="stat-num">867</div><div class="stat-label">Smart Phones</div></div>
  <div class="stat"><div class="stat-icon"><svg width="34" height="34" viewBox="0 0 34 34"><rect x="5" y="6" width="24" height="16" fill="none" stroke="#9a5a0d" stroke-width="2.5"/><path d="M17 22v5M11 28h12" stroke="#9a5a0d" stroke-width="2.5"/></svg></div><div class="stat-num">1904</div><div class="stat-label">Desktops</div></div>
  <div class="stat"><div class="stat-icon"><svg width="34" height="34" viewBox="0 0 34 34"><rect x="6" y="6" width="22" height="22" rx="2" fill="none" stroke="#9a5a0d" stroke-width="2.5"/><rect x="10" y="10" width="14" height="12" fill="#9a5a0d"/></svg></div><div class="stat-num">511</div><div class="stat-label">Tablets</div></div>
  <div class="stat"><div class="stat-icon"><svg width="34" height="34" viewBox="0 0 34 34"><circle cx="17" cy="17" r="6" fill="none" stroke="#9a5a0d" stroke-width="2.5"/><path d="M17 5v5M17 24v5M5 17h5M24 17h5M9 9l3 3M22 22l3 3M9 25l3-3M22 12l3-3" stroke="#9a5a0d" stroke-width="2.5"/></svg></div><div class="stat-num">2456</div><div class="stat-label">Software Installation</div></div>
</section>

<section class="why">
  <h2 class="section-title">WHY WE ARE THE BEST</h2>
  <p>The one stop comprehensive diagnostic &amp; repair station for your computer and connected devices.<br>We'll fix anything!</p>
  <div class="why-cards">
    <div class="why-card"><div class="card-photo" role="img" aria-label="Hands holding a smartphone with glowing network lines" style="background:linear-gradient(160deg,#1d3f66,#0c1a2e)"></div><div class="card-label">DIAGNOSIS &amp; REPAIR</div></div>
    <div class="why-card text-card"><h3>SETUP &amp; INSTALL</h3><p>Confused and frustrated with device setup &amp; installation? Leave it to the experts, which means all you've to do is sit back &amp; relax.</p></div>
    <div class="why-card"><div class="card-photo" role="img" aria-label="Technician working on a laptop" style="background:linear-gradient(160deg,#4d7fa8,#1f3d5c)"></div><div class="card-label">OPTIMIZATION</div></div>
    <div class="why-card top-label"><div class="card-photo" role="img" aria-label="Connected network of web icons on a blue background" style="background:linear-gradient(160deg,#3a8ec4,#12406a)"></div><div class="card-label">WEB DESIGNING</div></div>
  </div>
</section>

<section class="services">
  <h2 class="section-title">BEST SERVICES <small>That's What We Do</small></h2>
  <div class="service-list">
    <div class="service"><div class="service-icon"><svg width="44" height="44" viewBox="0 0 44 44"><circle cx="22" cy="16" r="8" fill="#fff"/><path d="M8 38c2-9 8-12 14-12s12 3 14 12z" fill="#fff"/></svg></div><h3>TECH SUPPORT</h3><p>We make technology easier for you with instant support.</p></div>
    <div class="service"><div class="service-icon"><svg width="44" height="44" viewBox="0 0 44 44"><path d="M12 28a8 8 0 0 1 2-16 10 10 0 0 1 18 3 7 7 0 0 1 0 13" fill="none" stroke="#fff" stroke-width="3"/><path d="M22 20v16M16 30l6 6 6-6" stroke="#fff" stroke-width="3" fill="none"/></svg></div><h3>DOWNLOADS</h3><p>The best apps to optimize &amp; secure your digital devices.</p></div>
    <div class="service"><div class="service-icon"><svg width="44" height="44" viewBox="0 0 44 44"><rect x="8" y="10" width="28" height="20" fill="none" stroke="#fff" stroke-width="3"/><path d="M4 34h36" stroke="#fff" stroke-width="3"/><path d="M18 24l8-8" stroke="#fff" stroke-width="2.5"/></svg></div><h3>WEB DESIGN</h3><p>We understand that every business owner has his own way of showcasing products</p></div>
    <div class="service"><div class="service-icon"><svg width="44" height="44" viewBox="0 0 44 44"><rect x="5" y="14" width="34" height="18" fill="#fff"/><path d="M22 17v12M16 23h12" stroke="#9a5a0d" stroke-width="3.5"/><circle cx="13" cy="34" r="3" fill="#fff"/><circle cx="31" cy="34" r="3" fill="#fff"/></svg></div><h3>UNDERSTAND THE<br>URGENCY</h3><p>We believe in careful planning for you</p></div>
  </div>
</section>

<section class="testimonials">
  <h2 class="section-title">WHAT OUR CLIENTS SAID</h2>
  <div class="client-photo" role="img" aria-label="Portrait of client Maren Holt"></div>
  <div class="client-name">Maren Holt</div>
  <span class="quote-mark" style="left:308px">&ldquo;</span>
  <p class="quote">Thank for such a Support. Quality Support. I'm extremely impressed. It has been one of the best experiences.So pleased with u Brondellix.You r d best.</p>
  <span class="quote-mark" style="left:872px">&rdquo;</span>
  <div class="dots"><i class="on"></i><i></i><i></i><i></i></div>
</section>

<section class="pricing">
  <h2 class="section-title">BEST PRICES <small>Our Affordable Prices</small></h2>
  <div class="plans">
    <div class="plan quick">
      <div class="plan-head"><span>QUICK FIX</span><small>1 Month</small></div>
      <div class="plan-price">NZD 95<br>USD 60*<br>GBP 40*</div>
      <p class="plan-note">*The price advertised might not be the same price charged to the credit card account due to exchange rate fluctuations. This means that because we are based in New Zealand we have to convert your purchase to New Zealand dollars at the exchange rate on the day it is processed.</p>
      <ul class="plan-features"><li>1 Month Tech Support</li><li>For 1 Computer</li><li>24X7 Availability</li></ul>
      <div class="plan-terms"><i></i>I agree to the Terms and Conditions</div>
      <div class="plan-order">ODER NOW</div>
    </div>
    <div class="plan starter">
      <div class="plan-head"><span>STARTER</span><small>6 Month</small></div>
      <div class="plan-price">NZD 140<br>USD 90*<br>GBP 60*</div>
      <p class="plan-note">*The price advertised might not be the same price charged to the credit card account due to exchange rate fluctuations. This means that because we are based in New Zealand we have to convert your purchase to New Zealand dollars at the exchange rate on the day it is processed.</p>
      <ul class="plan-features"><li>6 Month Tech Support</li><li>6 Month support for the same issue</li><li>24X7 Availability</li></ul>
      <div class="plan-terms"><i></i>I agree to the Terms and Conditions</div>
      <div class="plan-order">ODER NOW</div>
    </div>
    <div class="plan yearly">
      <div class="plan-head"><span>STARTER</span><small>1 Year</small></div>
      <div class="plan-price">NZD 250<br>USD 160*<br>GBP 105*</div>
      <p class="plan-note">*The price advertised might not be the same price charged to the credit card account due to exchange rate fluctuations. This means that because we are based in New Zealand we have to convert your purchase to New Zealand dollars at the exchange rate on the day it is processed.</p>
      <ul class="plan-features"><li>1 Year Tech Support</li><li>Upto 3 Computers &amp; Printers</li><li>Connected Devices with Router</li></ul>
      <div class="plan-terms"><i></i>I agree to the Terms and Conditions</div>
      <div class="plan-order">ODER NOW</div>
    </div>
  </div>
</section>

<section class="contact">
  <div class="map" role="img" aria-label="Street map of the city centre with the office location marked"></div>
  <h2 class="section-title">GET IN TOUCH <small>We are happy to talk with you.</small></h2>
  <div class="contact-cards">
    <div class="contact-card addr"><div class="contact-icon"><svg width="22" height="28" viewBox="0 0 22 28"><path d="M11 27S2 15 2 10a9 9 0 0 1 18 0c0 5-9 17-9 17z" fill="#fff"/><circle cx="11" cy="10" r="3.5" fill="#050505"/></svg></div><b>ADDRESS</b>Brondellix Services Ltd<br>Kestrel House Level 2<br>18 Marlow Lane<br>Harbour Central<br>Wellbridge 1011, New Zealand</div>
    <div class="contact-card phone"><div class="contact-icon"><svg width="26" height="26" viewBox="0 0 26 26"><path d="M6 3l4 1 2 6-3 2a14 14 0 0 0 5 5l2-3 6 2 1 4c-1 2-3 3-5 3C10 23 3 16 3 8c0-2 1-4 3-5z" fill="#fff"/></svg></div><b>PHONE</b>USA : +1 555 010 4821<br>UK : +44 20 7946 0312<br>AUS : +61 2 9100 5734</div>
    <div class="contact-card mail"><div class="contact-icon"><svg width="26" height="26" viewBox="0 0 26 26"><text x="13" y="20" text-anchor="middle" font-family="Roboto,sans-serif" font-size="22" font-weight="700" fill="#fff">@</text></svg></div><b>EMAIL</b>For Query - info@brondellix.com<br>For Billing - billing@brondellix.com<br>For Support - support@brondellix.com</div>
  </div>
  <div class="socials" aria-label="Social media links"><span></span><span></span><span></span><span></span></div>
</section>

<section class="register">
  <h2 class="section-title">LET'S REGISTER</h2>
  <div class="form">
    <div class="field">First Name</div><div class="field">Last Name</div>
    <div class="field">Street Address</div><div class="field select">Country</div>
    <div class="field">State, City</div><div class="field">Zip</div>
    <div class="field">Phone Number</div><div class="field">Email Address</div>
  </div>
  <div class="submit">REGISTER</div>
</section>

<footer class="site-footer">
  <div class="footer-brand"><span class="brand-mark"></span><span class="brand-name">Brondellix</span></div>
  <div class="copyright">Copyright © 2016 All rights Reserved</div>
  <nav class="footer-nav"><span class="active">HOME</span><span>SERVICES</span><span>PRICING</span><span>ABOUT US</span><span>CONTACT</span></nav>
</footer>

</body>
</html>
```